Pediatric Vision Care: Myopia Control Brochure

We are a pediatric eye care practice (ophthalmology and optometry). One of our services we offer for children is myopia control, which are strategies for slowing or stopping the progression of nearsightedness. This is a service we need to sell to parents because most insurance won't pay for it. There are different options we offer that can work well for kids in different situations: glasses with Corvane lenses, atropine eye drops, and/or special contact lenses. We need a brochure we can distribute to parents to let them know about this service that would encourage them to buy it for children who need it. Attached is our initial draft brochure created by our staff that provides text that we want to keep. The images and layout can change. We probably need at least one or two photos of kids on the brochure, because this is only something that works for children who are still growing, and the target audience is parents of 4-8 year old children.

Target Market(s)

Parents of 4-8 year old children

Font styles to use
Sans Serif

Requirements
Must have
• I'm uploading our company logo that should be included somewhere on the brochure. You can include contact information (web address, phone number) for our practice that is found on our website: http://www.brookhollowkidsvision.com/
Should not have
• This should not look childish. We need the impression to be friendly but professional, medical, expert.

```html
<!DOCTYPE html>
<html lang="en">
<head>
<meta charset="utf-8">
<title>Myopia Control Brochure – Brookhollow Kids Vision</title>
<link href="https://fonts.googleapis.com/css2?family=Montserrat:wght@400;500;600;700&display=swap" rel="stylesheet">
<style>
:root{
  --periwinkle:#6a7bd9;
  --lime:#9dd600;
  --sun:#fcc51d;
  --orange:#ff8a00;
  --ink:#1f1f24;
  --paper:#ffffff;
  --stage:#7b7b7b;
}
*{margin:0;padding:0;box-sizing:border-box}
html,body{width:1200px;height:2546px;overflow:hidden}
body{background:var(--stage);font-family:"Montserrat",Arial,sans-serif;color:var(--ink);position:relative}
.spread-frame{position:absolute;left:40px;width:1120px;height:798px;box-shadow:0 10px 24px rgba(0,0,0,.35)}
.spread-frame.outside{top:380px}
.spread-frame.inside{top:1330px}
.spread{position:absolute;left:0;top:0;width:852px;height:607px;transform:scale(1.3146);transform-origin:0 0;background:var(--paper);overflow:hidden}
.art{position:absolute;left:0;top:0;width:852px;height:607px}
.block{position:absolute}
.body-copy{font-size:10.6px;line-height:13.9px;text-align:justify;font-weight:500}
.body-copy p+p{margin-top:13px}
.panel-title{font-weight:600;line-height:1.05}
.white{color:#fff}
.peri{color:var(--periwinkle)}

/* outside */
.env-title{left:28px;top:57px;font-size:20.5px;color:#fff;font-weight:500}
.env-copy{left:27px;top:144px;width:234px}
.contact-title{left:306px;top:156px;font-size:20.5px;color:#fff;font-weight:500;line-height:24px}
.contact-list{left:306px;top:248px;width:250px;color:#fff}
.contact-label{font-size:13.5px;font-weight:500;margin-top:14px}
.contact-label:first-child{margin-top:0}
.contact-row{display:flex;align-items:center;margin-top:7px;font-size:10.8px;font-weight:500;line-height:17.5px}
.contact-row svg{width:16px;height:16px;margin:0 12px 0 12px;flex:none}
.brand{left:590px;top:300px;width:250px;text-align:center;font-size:19px;font-weight:600;color:var(--periwinkle);line-height:22px}
.myopia-title{left:590px;top:356px;width:250px;text-align:center;font-size:23px;font-weight:600;color:var(--periwinkle)}
.myopia-copy{left:592px;top:392px;width:238px;font-size:9.6px;line-height:13.7px}

/* inside */
.option-head{display:flex;align-items:flex-start;gap:12px}
.option-head svg{flex:none}
.option-title{font-size:21px;font-weight:600;line-height:22px}
.option-copy{font-size:10.6px;line-height:16.8px;font-weight:500}
.option-copy p+p{margin-top:16px}
.glasses{left:26px;top:26px;width:250px}
.glasses .option-copy{margin-top:20px}
.atropine{left:312px;top:301px;width:240px}
.atropine .option-copy{margin-top:18px;font-size:10.4px;line-height:14.8px;color:#fff}
.lenses{left:596px;top:26px;width:240px}
.lenses .option-copy{margin-top:26px}
</style>
</head>
<body>

<!-- Outside spread -->
<div class="spread-frame outside">
  <section class="spread">
    <svg class="art" viewBox="0 0 852 607" aria-hidden="false">
      <defs>
        <linearGradient id="examPhoto" x1="0" y1="0" x2="1" y2="1">
          <stop offset="0" stop-color="#c9d3e6"/>
          <stop offset=".5" stop-color="#e2d5c6"/>
          <stop offset="1" stop-color="#b58d63"/>
        </linearGradient>
        <linearGradient id="familyPhoto" x1="0" y1="0" x2="1" y2="1">
          <stop offset="0" stop-color="#f3f3f2"/>
          <stop offset=".6" stop-color="#e4ddd6"/>
          <stop offset="1" stop-color="#c9c7c6"/>
        </linearGradient>
      </defs>
      <rect x="440" y="0" width="412" height="320" fill="url(#examPhoto)" role="img" aria-label="Photo of a young girl at an eye exam machine"/>
      <rect x="0" y="425" width="285" height="182" fill="url(#familyPhoto)" role="img" aria-label="Photo of a smiling eye doctor holding a young girl in a clinic"/>
      <path d="M0 0 H560 C520 20 480 28 420 30 C350 32 300 34 285 36 L0 52 Z" fill="var(--periwinkle)"/>
      <path d="M0 52 C110 42 210 34 288 34 L334 104 C230 98 120 110 0 140 Z" fill="var(--lime)"/>
      <rect x="285" y="100" width="284" height="507" fill="var(--periwinkle)"/>
      <path d="M290 34 C400 30 500 48 592 100 L575 114 C480 92 390 92 334 104 Z" fill="var(--sun)"/>
      <path d="M292 34 L336 104" stroke="#fff" stroke-width="1.5"/>
      <path d="M592 100 C690 150 790 230 852 290 L852 307 C770 262 670 226 569 226 L569 118 Z" fill="var(--orange)"/>
      <path d="M569 226 C670 226 770 262 852 307 V607 H569 Z" fill="var(--paper)"/>
      <rect x="569" y="600" width="283" height="7" fill="var(--periwinkle)"/>
    </svg>

    <h2 class="block panel-title env-title">Environmental<br>options:</h2>
    <div class="block body-copy env-copy">
      <p>All myopic children can benefit from these lifestyle changes. It is important to get your child outdoors consistently. There is strong evidence that children who spend at least 2 hours a day outdoors are less likely to become myopic, and their myopia progresses slower than children who are outdoors less. Some studies show that increasing outdoor time by as few as 45minutes a day is beneficial in reducing progression.</p>
      <p>There is some evidence that consistent use of screens, particularly held very close to the face, can worsen nearsightedness. We recommend limiting nonacademic screen time and near work, and encourage your child to use the 20-20-20 rule. Every 20 minutes take a 20 second break to look at least 20 feet away.</p>
    </div>

    <h2 class="block contact-title">Contact and<br>scheduling info</h2>
    <div class="block contact-list">
      <div class="contact-label">Telephone</div>
      <div class="contact-row">
        <svg viewBox="0 0 24 24" fill="none" stroke="#fff" stroke-width="2" stroke-linecap="round" stroke-linejoin="round"><path d="M5 3h4l2 5-2.5 1.5a11 11 0 0 0 6 6L16 13l5 2v4a2 2 0 0 1-2 2A16 16 0 0 1 3 5a2 2 0 0 1 2-2z"/></svg>
        <span>Voice: (555) 204-0050<br>Text: (555) 204-3003</span>
      </div>
      <div class="contact-label">Mailing Address</div>
      <div class="contact-row">
        <svg viewBox="0 0 24 24" fill="none" stroke="#fff" stroke-width="2"><path d="M12 22s7-7 7-12a7 7 0 0 0-14 0c0 5 7 12 7 12z"/><circle cx="12" cy="10" r="2.5"/></svg>
        <span>Brookhollow Kids Vision<br>1280 Harbor Crest Drive<br>Norfolk, VA 23510</span>
      </div>
      <div class="contact-label">Email</div>
      <div class="contact-row">
        <svg viewBox="0 0 24 24" fill="none" stroke="#fff" stroke-width="2" stroke-linejoin="round"><rect x="3" y="5" width="18" height="14"/><path d="M3 5l9 8 9-8M3 19l7-7M21 19l-7-7"/></svg>
        <span>info@brookhollowkidsvision.com</span>
      </div>
      <div class="contact-label">Web</div>
      <div class="contact-row">
        <svg viewBox="0 0 24 24" fill="none" stroke="#fff" stroke-width="1.8"><circle cx="12" cy="12" r="9"/><ellipse cx="12" cy="12" rx="4" ry="9"/><path d="M3 12h18"/></svg>
        <span>www.brookhollowkidsvision.com</span>
      </div>
    </div>

    <div class="block brand">Brookhollow Kids Vision</div>
    <h1 class="block myopia-title">Myopia control</h1>
    <div class="block body-copy myopia-copy">
      <p>Myopia or nearsightedness causes blurry distance vision. Myopia is caused by the elongation of the eye, and progresses throughout childhood. Myopia is becoming increasingly common. More severe myopia and a higher glasses prescription is associated with a higher risk of eye problems involving the retina in adulthood, such as retinal problems and macular degeneration.Myopia control is meant to slow the growth of the eye, keeping the glasses prescription as low as possible and reducing the risk of ocular disease in adulthood. There are several treatment options</p>
    </div>
  </section>
</div>

<!-- Inside spread -->
<div class="spread-frame inside">
  <section class="spread">
    <svg class="art" viewBox="0 0 852 607">
      <defs>
        <linearGradient id="dropperPhoto" x1="0" y1="0" x2="1" y2="1">
          <stop offset="0" stop-color="#2c3b46"/>
          <stop offset=".5" stop-color="#4d6270"/>
          <stop offset="1" stop-color="#25323b"/>
        </linearGradient>
        <linearGradient id="fittingPhoto" x1="0" y1="0" x2="1" y2="1">
          <stop offset="0" stop-color="#8a6a55"/>
          <stop offset=".5" stop-color="#d8c3b3"/>
          <stop offset="1" stop-color="#6f7a7a"/>
        </linearGradient>
        <linearGradient id="contactPhoto" x1="0" y1="0" x2="1" y2="1">
          <stop offset="0" stop-color="#e9ddd3"/>
          <stop offset=".6" stop-color="#ebcdb8"/>
          <stop offset="1" stop-color="#d9b8a1"/>
        </linearGradient>
      </defs>
      <rect x="285" y="0" width="284" height="280" fill="url(#dropperPhoto)" role="img" aria-label="Photo of a glass eye dropper releasing a drop"/>
      <rect x="0" y="280" width="285" height="327" fill="url(#fittingPhoto)" role="img" aria-label="Photo of a woman trying on eyeglasses at an optician"/>
      <rect x="569" y="280" width="283" height="327" fill="url(#contactPhoto)" role="img" aria-label="Close-up photo of a contact lens being placed on an eye"/>
      <rect x="285" y="280" width="284" height="327" fill="var(--lime)"/>
      <path d="M0 372 C130 470 300 560 520 585 C560 589 585 588 605 585 C560 600 520 604 470 604 C300 604 150 590 0 560 Z" fill="var(--periwinkle)"/>
      <path d="M520 585 C560 589 585 588 605 585" stroke="#fff" stroke-width="1" fill="none" opacity=".6"/>
    </svg>

    <div class="block glasses">
      <div class="option-head">
        <svg width="44" height="34" viewBox="0 0 44 34" fill="none" stroke="#1f1f24" stroke-width="2.4" stroke-linecap="round"><circle cx="10" cy="22" r="8"/><circle cx="34" cy="22" r="8"/><path d="M18 21c2-2 6-2 8 0M4 16L10 4M40 16L34 4"/></svg>
        <h2 class="option-title peri">Halden Corvane<br>Glasses lenses</h2>
      </div>
      <div class="option-copy">
        <p>FDA market authorized Halden Corvane glasses lenses have been shown to slow myopia progression by about 50% in children aged 6-12.</p>
        <p>These lenses are a great treatment option because all your child needs to do is wear glasses. They look almost identical to ordinary glasses, but use specialized optics to signal the brain to slow the growth of myopic eyes.</p>
      </div>
    </div>

    <div class="block atropine">
      <div class="option-head">
        <svg width="34" height="36" viewBox="0 0 34 36" fill="none" stroke="#1f1f24" stroke-width="2" stroke-linecap="round" stroke-linejoin="round"><path d="M22 3l9 9M25 6l-14 14-4-4L21 2M11 20l-5 5"/><path d="M6 28c-2 3-3 4-3 5.5a2.5 2.5 0 0 0 5 0C8 32 7 31 6 28z"/></svg>
        <h2 class="option-title white">Low-dose<br>atropine</h2>
      </div>
      <div class="option-copy">
        <p>These eyedrops have been studied for over 20 years and have been shown to slow myopia progression by about 50% when used consistently.</p>
        <p>Low-dose atropine is simple to add to your daily routine. One drop is placed in each eye before bed each evening. These are ordered from a compounding pharmacy and mailed directly to your home.</p>
      </div>
    </div>

    <div class="block lenses">
      <div class="option-head">
        <svg width="46" height="40" viewBox="0 0 46 40" fill="none" stroke="#1f1f24" stroke-width="2" stroke-linecap="round"><path d="M6 20c5-8 11-12 17-12s12 4 17 12c-5 8-11 12-17 12S11 28 6 20z"/><circle cx="23" cy="20" r="6"/><path d="M23 2v3M10 6l2 3M36 6l-2 3M3 12l3 2M43 12l-3 2"/></svg>
        <h2 class="option-title peri">Specialty<br>contact lenses</h2>
      </div>
      <div class="option-copy">
        <p>FDA-approved Lumara lenses have been shown to slow myopia progression by about 50% in children aged 8-12.</p>
        <p>Contact lenses can be a great fit for many children, especially active children or those who do not enjoy wearing glasses. Many children as young as 7 or</p>
      </div>
    </div>
  </section>
</div>

</body>
</html>
```